Dune Air & Plus business card

I need an awesome, double-sided business card designed with our new logo. I would like the one side black with the colored logo, and the back side is all yours. I'd like to see horizontal and vertical layouts. Get creative! Thank you.

Target Market(s)

HVAC, Heating and Cooling in Phoenix, AZ

Industry/Entity Type

HVAC

Contact Information for Business Card

We need our new logo on the card. Tom Harker, (623) 555-0142, tom@trydunesair.com, www.trydunesair.com, ROC 514273

```html
<!DOCTYPE html>
<html lang="en">
<head>
<meta charset="utf-8">
<title>Dune Air &amp; Plus – Business Card</title>
<link href="https://fonts.googleapis.com/css2?family=Montserrat:wght@400;600;800&display=swap" rel="stylesheet">
<style>
  :root {
    --stage: #2b2b2d;
    --card-dark: #000000;
    --card-light: #ffffff;
    --brand-blue: #0a6fc2;
    --brand-orange: #ef7f1a;
    --ink: #1d1d1f;
  }
  * { box-sizing: border-box; margin: 0; padding: 0; }
  html, body {
    width: 1200px; height: 1024px; overflow: hidden;
    background: var(--stage);
    font-family: "Montserrat", sans-serif;
  }
  .stage {
    width: 1200px; height: 1024px;
    display: flex; flex-direction: column; align-items: center; justify-content: center;
    gap: 40px;
  }
  .card {
    width: 770px; height: 440px; position: relative; overflow: hidden;
    box-shadow: 0 12px 30px rgba(0,0,0,.45);
  }

  /* Front side */
  .card-front { background: var(--card-dark); }
  .front-brand {
    position: absolute; top: 70px; right: 70px;
    font-weight: 800; font-size: 46px; letter-spacing: 1px;
    color: var(--brand-blue); text-transform: uppercase;
  }
  .front-art {
    position: absolute; left: 0; right: 0; bottom: 0; height: 250px;
    background: linear-gradient(100deg, #0b74cc 0%, #0a6fc2 45%, #e0521f 75%, #f29224 100%);
  }

  /* Back side */
  .card-back { background: var(--card-light); color: var(--ink); }
  .holder {
    position: absolute; top: 56px; right: 60px; text-align: right;
  }
  .holder-name {
    font-weight: 600; font-size: 38px; text-transform: uppercase; letter-spacing: .5px;
  }
  .holder-name .first { color: var(--brand-blue); }
  .holder-name .last { color: var(--brand-orange); }
  .holder-role { font-size: 20px; margin-top: 2px; }

  .back-brand {
    position: absolute; top: 150px; left: 70px;
    display: flex; align-items: center; gap: 14px;
  }
  .back-brand-dot { width: 34px; height: 34px; border-radius: 50%; background: var(--brand-orange); }
  .back-brand-name {
    font-weight: 800; font-size: 36px; color: var(--brand-blue); text-transform: uppercase;
  }

  .contact {
    position: absolute; left: 70px; bottom: 48px;
    list-style: none; font-size: 21px; line-height: 1.55;
  }
  .contact li { display: flex; align-items: center; gap: 10px; }
  .license-label { color: var(--brand-blue); font-weight: 600; }
  .icon {
    width: 22px; height: 22px; border-radius: 50%; background: var(--brand-orange);
    display: inline-flex; align-items: center; justify-content: center; flex: none;
  }
  .icon svg { width: 13px; height: 13px; }
</style>
</head>
<body>
<main class="stage">

  <section class="card card-front" aria-label="Card front">
    <div class="front-brand">Dune Air &amp; Plus</div>
    <div class="front-art" role="img" aria-label="Illustration of a house with a garage door, flames and cooling lines in blue and orange"></div>
  </section>

  <section class="card card-back" aria-label="Card back">
    <div class="holder">
      <div class="holder-name"><span class="first">Tom</span> <span class="last">Harker</span></div>
      <div class="holder-role">Manager</div>
    </div>

    <div class="back-brand">
      <span class="back-brand-dot"></span>
      <span class="back-brand-name">Dune Air &amp; Plus</span>
    </div>

    <ul class="contact">
      <li><span><span class="license-label">ROC</span> 514273</span></li>
      <li>
        <span class="icon"><svg viewBox="0 0 24 24" fill="#fff"><path d="M6.6 10.8a15 15 0 0 0 6.6 6.6l2.2-2.2c.3-.3.7-.4 1-.2 1.1.4 2.3.6 3.6.6.6 0 1 .4 1 1V20c0 .6-.4 1-1 1A17 17 0 0 1 3 4c0-.6.4-1 1-1h3.5c.6 0 1 .4 1 1 0 1.3.2 2.5.6 3.6.1.3 0 .7-.2 1z"/></svg></span>
        (623) 555-0142
      </li>
      <li>
        <span class="icon"><svg viewBox="0 0 24 24" fill="none" stroke="#fff" stroke-width="2.4"><rect x="3" y="5" width="18" height="14" rx="1"/><path d="M3 6l9 7 9-7"/></svg></span>
        tom@trydunesair.com
      </li>
      <li>
        <span class="icon"><svg viewBox="0 0 24 24" fill="none" stroke="#fff" stroke-width="2.2"><circle cx="12" cy="12" r="9"/><path d="M3 12h18M12 3c3 3 3 15 0 18M12 3c-3 3-3 15 0 18"/></svg></span>
        www.trydunesair.com
      </li>
    </ul>
  </section>

</main>
</body>
</html>
```